Business card

I need to make clear the my status by my works acceptance in academia and pop culture.

The format of the card in the pics uploaded is an approximation. Something new may work or you make just tweak this design to make it more powerful.

```html
<!DOCTYPE html>
<html lang="en">
<head>
<meta charset="utf-8">
<title>Business Card – Victor Hallorane</title>
<link href="https://fonts.googleapis.com/css2?family=Cinzel:wght@400&family=Gentium+Book+Plus:wght@400&family=Poppins:ital,wght@0,300;0,400;1,300;1,400&display=swap" rel="stylesheet">
<style>
  :root{
    --bg-top:#f8cdbd;
    --bg-bottom:#f8cba0;
    --heading:#5a3a2c;
    --ink:#111111;
    --ink-soft:#555555;
    --paper:#ffffff;
    --night:#000000;
    --light:#ffffff;
    --muted:#b5b5b5;
  }
  *{margin:0;padding:0;box-sizing:border-box}
  html,body{width:1200px;height:1200px;overflow:hidden}
  body{background:linear-gradient(180deg,var(--bg-top),var(--bg-bottom));position:relative;font-family:'Poppins',sans-serif}
  .sheet-title{position:absolute;top:76px;left:0;width:1200px;text-align:center;color:var(--heading);font-weight:300;font-size:34px;line-height:46px}
  .card{position:absolute;top:240px;width:443px;height:738px;box-shadow:0 2px 6px rgba(0,0,0,.18)}
  .card--front{left:138px;background:var(--paper);color:var(--ink)}
  .card--back{left:641px;background:var(--night);color:var(--light)}
  .line{position:absolute;left:0;right:0;text-align:center;white-space:nowrap}
  .serif{font-family:'Gentium Book Plus',serif}
  .caps{font-family:'Cinzel',serif}
  .italic{font-style:italic}
  .ornament{position:absolute;left:50%;transform:translateX(-50%);border-radius:10px}
  .card--front .ornament{background:linear-gradient(90deg,rgba(17,17,17,0),rgba(17,17,17,.75) 50%,rgba(17,17,17,0))}
  .card--back .ornament{background:linear-gradient(90deg,rgba(255,255,255,0),rgba(255,255,255,.85) 50%,rgba(255,255,255,0))}
  .rule{position:absolute;left:74px;width:296px;height:2px;background:var(--light)}
  .rule-thin{position:absolute;left:97px;width:304px;height:1.5px;background:var(--ink)}
  .muted{color:var(--muted)}
  .soft{color:var(--ink-soft)}
</style>
</head>
<body>
  <div class="sheet-title">Business Card - Mockup 3<br>Size: 2.0 in X 3.5in, Color Mode : CMYK</div>

  <section class="card card--front">
    <div class="line caps" style="top:60px;font-size:31px;">Victor Hallorane, <span style="font-size:17px">Ph.D</span></div>
    <div class="line italic soft" style="top:104px;font-size:13px;font-weight:300;">The Marlowe and Renner of Psychology &amp; History</div>
    <div class="ornament" role="img" aria-label="Flourish ornament with lotus centre" style="top:152px;width:328px;height:14px;"></div>

    <div class="line serif" style="top:207px;font-size:20px;">“The Laurel Prize is a Sure Thing”</div>
    <div class="line italic soft" style="top:240px;font-size:16px;font-weight:300;">Martin Ashby, Ph.D.</div>
    <div class="line italic" style="top:262px;font-size:12.5px;">~ Professor of Psychology, University of Northmere ~</div>

    <div class="line serif" style="top:308px;font-size:20px;line-height:27px;">“Victor has the ability to just<br>open his eyes and see the truth.”</div>
    <div class="line italic soft" style="top:376px;font-size:16px;font-weight:300;">Cognitive Scientist</div>
    <div class="line italic" style="top:398px;font-size:12.5px;">~ Kessler University ~</div>

    <div class="rule-thin" style="top:455px;left:70px"></div>
    <div class="ornament" role="img" aria-label="Lotus divider ornament" style="top:438px;width:36px;height:36px;border-radius:6px;background:var(--ink)"></div>

    <div class="line" style="top:525px;font-size:13px;line-height:18px;">14 Alder Row, Suite 310, Brookhaven,<br>Westland, 40219</div>
    <div class="line" style="top:591px;font-size:13px;">555-218-0147</div>
    <div class="line" style="top:615px;font-size:13px;">victor@hallorane-mail.com</div>
    <div class="line" style="top:640px;font-size:13px;">www.victor-hallorane.org</div>
  </section>

  <section class="card card--back">
    <div class="line caps" style="top:60px;font-size:34px;">Victor’s Bio-Psych</div>
    <div class="ornament" role="img" aria-label="Scrolling flourish ornament" style="top:122px;width:296px;height:14px;"></div>

    <div class="line italic muted" style="top:161px;font-size:13px;font-weight:300;">is fundemental to all museums such as:</div>
    <div class="line serif" style="top:181px;font-size:18px;line-height:23px;">The Aurelian, The Castellan,<br>The Grand Civic Museum</div>

    <div class="line italic muted" style="top:246px;font-size:13px;font-weight:300;">and the films such as:</div>
    <div class="line serif" style="top:262px;font-size:18px;line-height:23px;">Iron Meridian, Velvet Mask,<br>Ember And The Tide, River Quest</div>

    <div class="ornament" role="img" aria-label="Crown ornament" style="top:338px;width:34px;height:30px;border-radius:6px;background:var(--light)"></div>
    <div class="rule" style="top:369px"></div>

    <div class="line serif" style="top:388px;font-size:19px;">Victor Maybe</div>
    <div class="line serif" style="top:414px;font-size:19px;">The Greatest Genius in History</div>
    <div class="line italic muted" style="top:445px;font-size:12.5px;font-weight:300;">~ Cognitive Scientist, Kessler University ~</div>

    <div class="rule" style="top:483px"></div>
    <div class="ornament" role="img" aria-label="Scroll ornament" style="top:486px;width:34px;height:28px;border-radius:6px;background:var(--light)"></div>

    <div class="line italic muted" style="top:545px;font-size:16px;font-weight:300;line-height:20px;">A Royal Antiquities Museum Exhibition<br>Featured Victor’s Ideas</div>
    <div class="line italic muted" style="top:590px;font-size:16px;font-weight:300;line-height:20px;">Over 100 Studio Films<br>Use Victor’s ideas</div>
    <div class="line italic muted" style="top:635px;font-size:16px;font-weight:300;line-height:20px;">Victor’s Bio- Sociology Has Restructrued<br>The Liberal Arts</div>
  </section>
</body>
</html>
```